Tech Company Letterhead/Business Cards/Envelopes

We would like a new stationary design for a technology company that develops full turnkey solutions for governments related to Data, Identity Tracking, Fingerprinting, Passport Control, and Border Protection Systems.

We would like the stationary designs to include:

Letter Head
Business Cards
Envelopes

Target Market(s)

Corporate

Industry/Entity Type

Business

Contact Information for Business Card

Details to be shared with the winner.

Font styles to use
Serif
Sans Serif

Colors
e4daeb
85abd2
3176b5
0355a3
0692cd

```html
<!DOCTYPE html>
<html lang="en">
<head>
<meta charset="utf-8">
<title>Norvex Stationery</title>
<link href="https://fonts.googleapis.com/css2?family=Montserrat:wght@400;500;600&display=swap" rel="stylesheet">
<style>
  :root {
    --brand-blue: #0a6fb8;
    --brand-grey: #58585a;
    --paper: #ffffff;
    --backdrop: #e6e6e6;
    --text-dark: #3d3d3f;
    --faint-blue: #4d88c8;
  }
  * { margin: 0; padding: 0; box-sizing: border-box; }
  html, body { width: 1200px; height: 1194px; overflow: hidden; }
  body {
    background: var(--backdrop);
    font-family: "Montserrat", sans-serif;
    position: relative;
    color: var(--text-dark);
  }
  .piece { position: absolute; background: var(--paper); overflow: hidden; box-shadow: 0 4px 10px rgba(0,0,0,.18); }
  .swoosh { position: absolute; inset: 0; width: 100%; height: 100%; }
  .wordmark { position: absolute; font-weight: 600; color: var(--brand-blue); letter-spacing: .04em; line-height: 1; }
  .contact-list { position: absolute; list-style: none; }
  .contact-list li { display: flex; align-items: center; gap: 5px; }
  .contact-list svg { width: 8px; height: 8px; fill: none; stroke: var(--brand-blue); stroke-width: 1.6; }
  .contact-list .web-accent { color: var(--brand-blue); }
  .address { position: absolute; text-align: right; color: #fff; letter-spacing: .05em; }

  /* Letterhead */
  .letterhead { left: 46px; top: 78px; width: 525px; height: 679px; }
  .letterhead .wordmark { left: 26px; top: 18px; font-size: 44px; }
  .letterhead .contact-list { left: 26px; top: 62px; font-size: 10.5px; line-height: 13px; }
  .letterhead .rule { position: absolute; left: 26px; top: 119px; width: 473px; height: 1.5px; background: var(--brand-blue); }
  .letterhead .address { right: 26px; top: 630px; font-size: 13.5px; line-height: 17px; }

  /* Business card front */
  .card-front { left: 628px; top: 164px; width: 382px; height: 217px; border-radius: 14px; }
  .card-front .wordmark { left: 22px; top: 22px; font-size: 56px; }
  .card-front .notch { position: absolute; left: -13px; top: 114px; width: 26px; height: 26px; border-radius: 50%; background: var(--brand-grey); }
  .card-front .holder { position: absolute; left: 22px; top: 114px; }
  .holder-name { font-size: 14.5px; font-weight: 600; color: var(--brand-blue); line-height: 17px; }
  .holder-role { font-size: 9.5px; letter-spacing: .04em; }
  .card-front .contact-list { left: 22px; top: 150px; font-size: 9.5px; line-height: 12px; letter-spacing: .03em; }
  .card-front .address { right: 22px; top: 173px; font-size: 9.5px; line-height: 12px; }

  /* Business card back */
  .card-back { left: 628px; top: 483px; width: 382px; height: 217px; border-radius: 14px; background: var(--brand-blue); display: flex; align-items: center; justify-content: center; }
  .card-back .wordmark { position: static; color: #fff; font-size: 66px; }

  /* Envelope front */
  .envelope-front { left: 28px; top: 826px; width: 564px; height: 297px; background: transparent; box-shadow: none; overflow: visible; }
  .envelope-front .flap { position: absolute; left: 0; top: 0; width: 100%; height: 50px; background: var(--brand-blue); border-radius: 60px 60px 0 0; }
  .envelope-front .body { position: absolute; left: 0; top: 42px; width: 100%; height: 255px; background: var(--paper); overflow: hidden; box-shadow: 0 4px 10px rgba(0,0,0,.18); }
  .envelope-front .wordmark { left: 71px; top: 96px; font-size: 70px; }
  .envelope-front .address { right: 16px; top: 207px; font-size: 14.5px; line-height: 18px; }

  /* Envelope back */
  .envelope-back { left: 603px; top: 869px; width: 563px; height: 254px; background: var(--brand-blue); }
  .envelope-back .flap-edge { position: absolute; left: 0; top: 0; width: 100%; height: 43px; background: var(--paper); border-radius: 0 0 60px 60px; }
  .envelope-back .wordmark { left: 0; right: 0; top: 118px; text-align: center; font-size: 86px; color: var(--faint-blue); }
  .envelope-back .web { position: absolute; left: 0; right: 0; top: 227px; text-align: center; color: #fff; font-size: 15px; letter-spacing: .05em; }
</style>
</head>
<body>

<!-- Letterhead -->
<section class="piece letterhead">
  <svg class="swoosh" viewBox="0 0 525 679" preserveAspectRatio="none" aria-hidden="true">
    <path d="M40 679 Q420 640 525 536 L525 679 Z" fill="var(--brand-blue)"/>
    <path d="M60 679 Q440 650 525 571 L525 679 Z" fill="var(--brand-grey)"/>
  </svg>
  <div class="wordmark">NORVEX</div>
  <ul class="contact-list">
    <li><svg viewBox="0 0 10 10"><path d="M2 1 L4 3 L3 4.5 Q4.5 6.5 5.5 7 L7 6 L9 8 L7.5 9.5 Q2 8 0.8 2.5 Z"/></svg>02 5550 1400</li>
    <li><svg viewBox="0 0 10 10"><path d="M1 4 Q5 0 9 4 M2 5 h6 v4 h-6 Z"/></svg>1300 555 218</li>
    <li><svg viewBox="0 0 10 10"><rect x="1" y="2" width="8" height="6"/><path d="M1 2 L5 6 L9 2"/></svg>info@norvex.com</li>
    <li><svg viewBox="0 0 10 10"><circle cx="5" cy="5" r="4"/><path d="M1 5 h8 M5 1 v8"/></svg>www.<span class="web-accent">NORVEX</span>.com</li>
  </ul>
  <div class="rule"></div>
  <p class="address">Level 4, 12 Harbour<br>Street Sydney 2000 NSW</p>
</section>

<!-- Business card front -->
<section class="piece card-front">
  <svg class="swoosh" viewBox="0 0 382 217" preserveAspectRatio="none" aria-hidden="true">
    <path d="M338 0 Q330 185 112 217 L382 217 L382 0 Z" fill="var(--brand-blue)"/>
    <path d="M350 0 Q345 195 128 217 L382 217 L382 0 Z" fill="var(--brand-grey)"/>
  </svg>
  <div class="wordmark">NORVEX</div>
  <div class="notch"></div>
  <div class="holder">
    <p class="holder-name">Marcus Whitfield</p>
    <p class="holder-role">CEO &amp; Managing Director</p>
  </div>
  <ul class="contact-list">
    <li><svg viewBox="0 0 10 10"><path d="M2 1 L4 3 L3 4.5 Q4.5 6.5 5.5 7 L7 6 L9 8 L7.5 9.5 Q2 8 0.8 2.5 Z"/></svg>02 5550 1400</li>
    <li><svg viewBox="0 0 10 10"><path d="M1 4 Q5 0 9 4 M2 5 h6 v4 h-6 Z"/></svg>1300 555 218</li>
    <li><svg viewBox="0 0 10 10"><rect x="1" y="2" width="8" height="6"/><path d="M1 2 L5 6 L9 2"/></svg>info@norvex.com</li>
    <li><svg viewBox="0 0 10 10"><circle cx="5" cy="5" r="4"/><path d="M1 5 h8 M5 1 v8"/></svg>www.<span class="web-accent">NORVEX</span>.com</li>
  </ul>
  <p class="address">Level 4, 12 Harbour<br>Street Sydney 2000 NSW</p>
</section>

<!-- Business card back -->
<section class="piece card-back">
  <div class="wordmark">NORVEX</div>
</section>

<!-- Envelope front -->
<section class="piece envelope-front">
  <div class="flap"></div>
  <div class="body">
    <svg class="swoosh" viewBox="0 0 564 255" preserveAspectRatio="none" aria-hidden="true">
      <path d="M522 0 Q510 200 252 255 L564 255 L564 0 Z" fill="var(--brand-blue)"/>
      <path d="M533 0 Q525 215 270 255 L564 255 L564 0 Z" fill="var(--brand-grey)"/>
    </svg>
    <div class="wordmark">NORVEX</div>
    <p class="address">Level 4, 12 Harbour<br>Street Sydney 2000 NSW</p>
  </div>
</section>

<!-- Envelope back -->
<section class="piece envelope-back">
  <div class="flap-edge"></div>
  <div class="wordmark">NORVEX</div>
  <p class="web">www.NORVEX.com</p>
</section>

</body>
</html>
```